mobile app design: app provides timely Natural gas pipeline information (similar to weather, etc)

we are going to create and publish an app in all the three markets.( android, ios,windows). we have wire framed mostly all the screens. the designers are to provide the layout, design & background. The following are the most important things.

1. the app's target audience are guys working in the natural gas industry in the US.
2. the app provides the customer with latest pipeline information
3. the trial version is free and will provide information about one pipeline
4. slides 1 to 5 are trial version slides.
5. slides 6 onwards the customer chooses.
6. the final product is displayed in a grid.
7. the app will be developed using html5 and css3.
8. customer will pay per pipeline for the information. ( in app payment)
9 there are similiar ( complementary) products which provide weekly storage data at vendra shelf and bramlo soft bazaar.
10. i have attached the pdf document of the wireframe.
11.i have attached the logo
12. no name has been thought out yet.

Hi guys

I have a main question for the designer community .

1. is it possible to combine some of the pages ( screens  ) into one or two. use your gut feel. if not it is ok.

2. check out the flow, the color, the background , the font and the font size. it should be pleasing.

thanx

Tomek

```html
<!DOCTYPE html>
<html lang="en">
<head>
<meta charset="utf-8">
<title>Pipeline Selector</title>
<link rel="stylesheet" href="https://fonts.googleapis.com/css2?family=Arimo:wght@400;700&display=swap">
<style>
  :root {
    --page-bg: #111214;
    --brand-blue: #0b52a8;
    --white: #ffffff;
    --panel-gold: #e9c560;
    --panel-gold-edge: #d9b24c;
    --header-ink: #4a4636;
    --region: #e8744f;
    --region-line: #d9633f;
    --region-active: #e05a30;
    --region-active-edge: #c8461f;
    --type: #3bbfbf;
    --type-line: #31a9a9;
    --type-active: #1ea3a3;
    --scene-top: #dfe6ec;
    --scene-mid: #ecefef;
    --scene-bottom: #d7dcdc;
  }
  * { box-sizing: border-box; margin: 0; padding: 0; }
  html, body {
    width: 1200px; height: 2361px; overflow: hidden;
    background: var(--page-bg);
    font-family: "Arimo", Arial, sans-serif;
  }
  .screen {
    position: absolute; left: 0; top: 113px;
    width: 1200px; height: 2135px; overflow: hidden;
  }
  .status-bar {
    position: absolute; left: 0; top: 0; width: 1200px; height: 79px;
    background: var(--brand-blue); color: var(--white);
    font-size: 40px; display: flex; align-items: center; padding: 0 30px;
  }
  .status-left { display: flex; align-items: center; gap: 14px; }
  .signal { display: flex; gap: 5px; }
  .signal span { width: 17px; height: 17px; border-radius: 50%; border: 2px solid var(--white); }
  .signal span.on { background: var(--white); }
  .clock { position: absolute; left: 0; right: 0; text-align: center; font-weight: 700; pointer-events: none; }
  .status-right { margin-left: auto; display: flex; align-items: center; gap: 14px; }
  .battery { width: 84px; height: 34px; border: 3px solid var(--white); border-radius: 7px; padding: 3px; position: relative; }
  .battery::before { content: ""; display: block; width: 100%; height: 100%; background: var(--white); border-radius: 3px; }
  .battery::after { content: ""; position: absolute; right: -9px; top: 9px; width: 5px; height: 11px; background: var(--white); border-radius: 0 3px 3px 0; }
  .title-bar {
    position: absolute; left: 0; top: 79px; width: 1200px; height: 169px;
    background: var(--brand-blue); color: var(--white);
    font-size: 56px; font-weight: 700; text-align: center; line-height: 169px;
  }
  .backdrop {
    position: absolute; left: 0; top: 248px; width: 1200px; height: 1887px;
    background: linear-gradient(180deg, var(--scene-top) 0%, var(--scene-mid) 45%, var(--scene-bottom) 100%);
  }
  .selector {
    position: absolute; left: 130px; top: 639px; width: 921px; height: 1031px;
    background: var(--panel-gold); border: 2px solid var(--panel-gold-edge); border-radius: 4px;
  }
  .selector-divider { position: absolute; left: 457px; top: 0; bottom: 0; width: 2px; background: var(--panel-gold-edge); }
  .column-head {
    position: absolute; top: 0; height: 132px; line-height: 132px;
    font-size: 48px; color: var(--header-ink); text-align: center;
  }
  .column-head.region { left: 0; width: 457px; }
  .column-head.type { left: 459px; width: 460px; }
  .option {
    position: absolute; color: var(--white); font-size: 48px;
    display: flex; align-items: center; justify-content: center;
  }
  .option.region { left: 31px; width: 426px; height: 144px; background: var(--region); border-bottom: 2px solid var(--region-line); }
  .option.region.is-selected { background: var(--region-active); border: 5px solid var(--region-active-edge); }
  .option.type { left: 460px; width: 427px; height: 289px; background: var(--type); border-bottom: 2px solid var(--type-line); }
  .option.type.is-selected { background: var(--type-active); box-shadow: inset 0 0 18px rgba(0,60,60,0.45); border-bottom: none; }
  .next-button {
    position: absolute; left: 516px; top: 1952px; width: 107px; height: 107px;
    background: var(--brand-blue); border-radius: 22px;
    display: flex; align-items: center; justify-content: center;
  }
</style>
</head>
<body>
<main class="screen">
  <div class="status-bar">
    <div class="status-left">
      <div class="signal"><span class="on"></span><span class="on"></span><span class="on"></span><span></span><span></span></div>
      <span class="carrier">KESTA</span>
      <svg width="44" height="34" viewBox="0 0 44 34" aria-hidden="true">
        <path d="M22 31 L28 24 A9 9 0 0 0 16 24 Z" fill="#fff"/>
        <path d="M9 17 A19 19 0 0 1 35 17" stroke="#fff" stroke-width="5" fill="none" stroke-linecap="round"/>
        <path d="M3 10 A28 28 0 0 1 41 10" stroke="#fff" stroke-width="5" fill="none" stroke-linecap="round"/>
      </svg>
    </div>
    <div class="clock">4:21 PM</div>
    <div class="status-right">
      <span class="charge">100%</span>
      <div class="battery"></div>
    </div>
  </div>
  <header class="title-bar">Title</header>
  <div class="backdrop" role="img" aria-label="Pale photograph of natural gas plant pipework"></div>

  <section class="selector">
    <div class="selector-divider"></div>
    <div class="column-head region">Select Region</div>
    <div class="column-head type">Company Type</div>

    <div class="option region" style="top:132px">NorthEast</div>
    <div class="option region" style="top:276px">MidWest</div>
    <div class="option region is-selected" style="top:420px">Central</div>
    <div class="option region" style="top:564px">SouthEast</div>
    <div class="option region" style="top:708px">SouthWest</div>
    <div class="option region" style="top:852px">West</div>

    <div class="option type" style="top:132px">InterState</div>
    <div class="option type" style="top:421px">IntraState</div>
    <div class="option type is-selected" style="top:710px">OffShore</div>
  </section>

  <div class="next-button" aria-label="Next">
    <svg width="40" height="46" viewBox="0 0 40 46" aria-hidden="true">
      <path d="M12 7 L28 23 L12 39" stroke="#fff" stroke-width="7" fill="none" stroke-linecap="round" stroke-linejoin="round"/>
    </svg>
  </div>
</main>
</body>
</html>
```